Haldor Snekker AS
Buiness cards for haldor snekker as
Haldor Snekker AS - Construction
Creative Brief
Simple
Tobias Kranveldt
CEO
Lerkeskogveien 14 0587 OSLO Norway
post@haldorsnekker.example
www.haldorsnekker.example
Org. nr.: 836 402 517
Its for a company that expanse fast within big building sites
come up with something!?! we make your investment possible

```html
<!DOCTYPE html>
<html lang="en">
<head>
<meta charset="utf-8">
<title>Haldor Snekker AS — Business Cards</title>
<link rel="stylesheet" href="https://fonts.googleapis.com/css2?family=Libre+Baskerville:wght@400;700&display=swap">
<style>
  :root {
    --brand-red: #d8262b;
    --ink: #1c1c1c;
    --muted: #5a5a5a;
    --paper: #ffffff;
    --backdrop: #e6e6e4;
  }
  * { box-sizing: border-box; margin: 0; padding: 0; }
  html, body { width: 1200px; height: 998px; overflow: hidden; }
  body {
    background: var(--backdrop);
    font-family: "Libre Baskerville", Georgia, serif;
    position: relative;
  }
  .card {
    position: absolute;
    left: 220px;
    width: 760px;
    height: 434px;
    overflow: hidden;
    box-shadow: 0 10px 28px rgba(0,0,0,.18);
  }
  /* Front */
  .card--front { top: 52px; background: var(--brand-red); color: var(--paper); }
  .front__name {
    position: absolute; left: 56px; bottom: 92px;
    font-weight: 700; font-size: 40px; letter-spacing: 1px; line-height: 1;
  }
  .front__rule {
    position: absolute; left: 56px; bottom: 78px; width: 330px; height: 1px;
    background: rgba(255,255,255,.7);
  }
  .front__tagline {
    position: absolute; left: 56px; bottom: 52px;
    font-size: 15px; font-style: italic; letter-spacing: .5px;
  }
  /* Back */
  .card--back { top: 512px; background: var(--paper); color: var(--ink); }
  .brand {
    position: absolute; left: 48px; top: 52px;
    display: flex; align-items: center; gap: 14px;
  }
  .brand__mark { width: 30px; height: 30px; background: var(--brand-red); }
  .brand__name { font-weight: 700; font-size: 28px; color: var(--ink); letter-spacing: .5px; }
  .person {
    position: absolute; right: 48px; top: 118px; text-align: right;
  }
  .person__name { color: var(--brand-red); font-weight: 700; font-size: 24px; }
  .person__role { font-size: 14px; color: var(--muted); margin-top: 4px; }
  .person__details { font-size: 14px; line-height: 1.65; color: var(--muted); margin-top: 12px; }
  .bands { position: absolute; left: 0; top: 0; width: 760px; height: 434px; }
  .contacts {
    position: absolute; left: 48px; top: 252px; list-style: none;
    font-size: 14px; color: var(--muted); line-height: 1;
  }
  .contacts li { display: flex; align-items: center; gap: 12px; margin-bottom: 11px; }
  .contacts svg { width: 15px; height: 15px; fill: var(--brand-red); flex: none; }
  .web {
    position: absolute; left: 48px; bottom: 18px;
    font-size: 14px; color: var(--paper); letter-spacing: 2px;
  }
</style>
</head>
<body>
  <section class="card card--front">
    <div class="front__name">HALDOR SNEKKER AS</div>
    <div class="front__rule"></div>
    <div class="front__tagline">we make your investment possible</div>
  </section>

  <section class="card card--back">
    <svg class="bands" viewBox="0 0 760 434" aria-hidden="true">
      <polygon points="560,300 760,300 760,318 540,318" fill="#1c1c1c"/>
      <polygon points="0,380 760,380 760,434 0,434" fill="#d8262b"/>
      <polygon points="500,380 540,360 760,360 760,380" fill="#d8262b"/>
    </svg>

    <div class="brand">
      <span class="brand__mark"></span>
      <span class="brand__name">HALDOR SNEKKER AS</span>
    </div>

    <div class="person">
      <div class="person__name">Tobias Kranveldt</div>
      <div class="person__role">CEO</div>
      <div class="person__details">
        Org. nr.: 836 402 517<br>
        Lerkeskogveien 14<br>
        0587 OSLO, Norway
      </div>
    </div>

    <ul class="contacts">
      <li>
        <svg viewBox="0 0 24 24"><path d="M6.6 10.8a15.1 15.1 0 0 0 6.6 6.6l2.2-2.2a1 1 0 0 1 1-.25 11.4 11.4 0 0 0 3.6.57 1 1 0 0 1 1 1V20a1 1 0 0 1-1 1A17 17 0 0 1 3 4a1 1 0 0 1 1-1h3.5a1 1 0 0 1 1 1c0 1.25.2 2.45.57 3.57a1 1 0 0 1-.25 1z"/></svg>
        +47 22 04 18 60
      </li>
      <li>
        <svg viewBox="0 0 24 24"><path d="M7 2h10a2 2 0 0 1 2 2v16a2 2 0 0 1-2 2H7a2 2 0 0 1-2-2V4a2 2 0 0 1 2-2zm0 3v13h10V5zm5 14.2a1 1 0 1 0 0 .01z"/></svg>
        +47 48 21 93 05
      </li>
      <li>
        <svg viewBox="0 0 24 24"><path d="M3 5h18a1 1 0 0 1 1 1v12a1 1 0 0 1-1 1H3a1 1 0 0 1-1-1V6a1 1 0 0 1 1-1zm9 7.5L4 7.3V8l8 5.2L20 8v-.7z"/></svg>
        post@haldorsnekker.example
      </li>
    </ul>

    <div class="web">www.haldorsnekker.example</div>
  </section>
</body>
</html>
```